The Copper Meadow Brochure

WE HAVE CHANGED OUR BUSINESS NAME DUE THE ADDITION OF A PLANT NURSERY AND GIFTSHOP AND WANT TO MAKE THE LOCAL COMUNITY AWARE THAT WE ARE JUST NOT A PET SHOP AND STOCKFEEDS ANYMORE. OUR COLOURS A BLUE PINK AND GREEN, WE ARE OPEN 7 DAYS. I HAVE ATTACHED A DL FLYER I WAS PLAYING WITH MYSELF BUT I THINK a 3 FOLD A4 FLYER IS NOW OUR AIM WITH A BIT MORE GRAB TO IT. WE SELL PUPPIES, KITTENS, BIRDS, MICE, GUINEA PIGS AND ALL PET SUPPLIES.

THE PRODUCE STORE SELLS CHICKENS, CHOOKS, HAY AND STOCKFEED AS WELL AS BULK DOG FOOD. THE NURSERY SELLS PLANTS, POTS, GIFTWARE, STATUES POTTING MIX ETC.

OUR FACEBOOK PAGE HAS SOME PHOTOS AND I HAVE INDLUDED THE FLYER I STARTED WORKING ON.
Updates

Hello Designers We would like to change from 2 days to 5 days working time to allow you more time for a great design. We would like an A4 Brochure that folds into 3 (DL Size) with our logo on the front, one section for each area of the shop PETS, PLANTS and PRODUCE using the colour palet that is used in our logo. Keeping in mind the "PLANTS" is all new and we sell GIFTWARE in that section as well. Our opening hours on the back cover and a voucher on the middle section back cover stating 10% OFF Plants , Giftware and Pet Supplies. (in small print) dog food and vet meds not included.

Target Market(s)

Very Wide Demographic young old male and female, We want our variety to show through plus an additional draw card with a voucher on the back of the flyer to entice any new customers to come and view the store.

Industry/Entity Type

Business

Font styles to use
Other font styles liked:
• ariel or similar to logo

Colors
0493ce
9ccb3b
e34197

Requirements
Must have
• opening hours
attention to 'OPEN 7 DAYS A WEEK'
Huge Store
Very Good pricing
with our address we need the additional (OPPOSITE THE TALLOWBROOK STOCKYARDS)

```html
<!DOCTYPE html>
<html lang="en">
<head>
<meta charset="utf-8">
<title>The Copper Meadow – Tri-fold Brochure</title>
<link rel="stylesheet" href="https://fonts.googleapis.com/css2?family=Arimo:wght@400;700&family=Montserrat:wght@500;700&family=Satisfy&display=swap">
<style>
  :root{
    --blue:#0493ce;
    --green:#9ccb3b;
    --green-dark:#86b52c;
    --pink:#e34197;
    --brown:#9a5526;
    --grey-light:#f4f4f4;
    --ink:#1e1e1e;
    --paper-bg:#ece7e1;
  }
  *{box-sizing:border-box;margin:0;padding:0}
  html,body{width:828px;height:1200px;overflow:hidden;background:var(--paper-bg)}
  body{position:relative;font-family:"Arimo",Arial,sans-serif;color:var(--ink)}
  .sheet{position:absolute;left:25px;width:778px;overflow:hidden;background:var(--grey-light);box-shadow:0 2px 6px rgba(0,0,0,.18)}
  .sheet--outside{top:33px;height:547px}
  .sheet--inside{top:618px;height:549px}
  .sheet__art{position:absolute;inset:0;width:100%;height:100%}
  .abs{position:absolute}
  .center{text-align:center}

  /* outside */
  .voucher__badge{left:98px;top:283px;width:124px;height:124px;display:flex;align-items:center;justify-content:center;flex-direction:column;font-family:"Satisfy",cursive;color:#fff;font-size:33px;line-height:1}
  .voucher__items{left:40px;top:424px;width:180px;font-size:18px;line-height:23px}
  .voucher__small{left:0;top:528px;width:259px;font-size:13px}
  .hours{left:259px;top:26px;width:260px;font-size:16px;line-height:24px}
  .hours__title{font-family:"Montserrat",sans-serif;font-weight:700;font-size:16px}
  .brand{display:flex;align-items:center;gap:7px;font-family:"Montserrat",sans-serif;font-weight:700;color:var(--blue);white-space:nowrap}
  .brand__dot{width:14px;height:14px;border-radius:50%;background:var(--brown);flex:none}
  .brand--panel{left:259px;top:358px;width:260px;justify-content:center;font-size:18px}
  .brand--cover{left:519px;top:140px;width:259px;justify-content:center;font-size:19px}
  .contact{left:259px;top:484px;width:260px;font-family:"Montserrat",sans-serif;font-size:13px;line-height:17px}
  .contact__phone{font-weight:700;font-size:15px;margin-bottom:2px}
  .cover__tagline{left:519px;top:502px;width:259px;font-family:"Montserrat",sans-serif;font-weight:700;font-size:16px;line-height:22px}

  /* inside */
  .tag{position:absolute;height:20px;padding:0 20px 0 8px;background:var(--brown);color:#fff;font-family:"Satisfy",cursive;font-size:15px;line-height:20px;white-space:nowrap;clip-path:polygon(0 0,calc(100% - 12px) 0,100% 50%,calc(100% - 12px) 100%,0 100%)}
  .tag--pets{left:0;top:247px;width:80px}
  .tag--stock{left:0;top:308px;width:162px}
  .tag--produce{left:519px;top:215px;width:108px}
  .tag--grain{left:519px;top:349px;width:130px}
  .list{position:absolute;list-style:none;font-size:8px;line-height:12px;color:var(--ink)}
  .list li{padding-left:7px;text-indent:-7px}
  .list li::before{content:"• "}
  .list--pet-a{left:8px;top:270px;width:122px}
  .list--pet-b{left:134px;top:270px;width:124px}
  .list--stock-a{left:8px;top:331px;width:122px}
  .list--stock-b{left:134px;top:331px;width:122px}
  .list--white{color:#fff;font-size:10px}
  .list--plants{left:296px;top:176px;width:210px;line-height:13px}
  .list--plants li{margin-bottom:13px}
  .list--plants li.tight{margin-bottom:0}
  .list--produce li,.list--grain li{margin-bottom:8px}
  .list--produce{left:548px;top:248px}
  .list--grain{left:548px;top:379px}
  .fine{left:268px;top:374px;font-size:8.5px;color:#222}
</style>
</head>
<body>

<section class="sheet sheet--outside" aria-label="Brochure outside">
  <svg class="sheet__art" viewBox="0 0 778 547">
    <defs>
      <linearGradient id="g-grey" x1="0" y1="0" x2="1" y2="0"><stop offset="0" stop-color="#ececec"/><stop offset=".5" stop-color="#fafafa"/><stop offset="1" stop-color="#e2e2e2"/></linearGradient>
      <linearGradient id="g-nursery" x1="0" y1="0" x2="0" y2="1"><stop offset="0" stop-color="#8fb4d8"/><stop offset=".35" stop-color="#4f7a3a"/><stop offset=".75" stop-color="#c7608f"/><stop offset="1" stop-color="#cdbf4a"/></linearGradient>
      <linearGradient id="g-family" x1="0" y1="0" x2="1" y2="1"><stop offset="0" stop-color="#8b8f57"/><stop offset=".5" stop-color="#e9dcc4"/><stop offset="1" stop-color="#b9c27a"/></linearGradient>
    </defs>
    <rect x="0" y="0" width="778" height="547" fill="url(#g-grey)"/>
    <path d="M200 0 H519 V140 C450 175 360 150 270 175 C250 180 235 185 225 190 Z" fill="var(--green)"/>
    <path d="M225 190 C300 160 420 170 519 150 V175 C420 195 320 180 240 205 Z" fill="#fff"/>
    <path d="M240 205 C320 182 420 195 519 175 V188 C420 205 320 195 245 215 Z" fill="var(--blue)"/>
    <path d="M0 0 H250 C285 130 265 265 185 320 C130 350 60 352 0 340 Z" fill="url(#g-nursery)" role="img" aria-label="Photo of the plant nursery with flowering shrubs and a shade house"/>
    <path d="M250 0 C285 130 265 265 185 320 C130 350 60 352 0 340" fill="none" stroke="var(--blue)" stroke-width="6"/>
    <circle cx="160" cy="345" r="62" fill="var(--brown)" stroke="var(--green)" stroke-width="6"/>
    <path d="M259 415 C360 428 440 440 519 452 V470 C440 458 360 448 259 438 Z" fill="var(--blue)"/>
    <path d="M259 438 C360 448 440 458 519 470 V478 C440 468 360 458 259 452 Z" fill="#fff"/>
    <path d="M259 452 C360 460 440 470 519 478 V547 H259 Z" fill="var(--green)"/>
    <path d="M519 222 C610 225 700 205 778 170 V200 C700 232 610 250 519 250 Z" fill="var(--blue)"/>
    <path d="M519 250 C610 250 700 232 778 200 V447 H519 Z" fill="url(#g-family)" role="img" aria-label="Photo of a young girl cuddling a golden retriever puppy"/>
    <path d="M519 447 H778 V462 C700 470 610 476 519 470 Z" fill="var(--blue)"/>
    <path d="M519 470 C610 476 700 470 778 462 V547 H519 Z" fill="var(--green)"/>
  </svg>

  <div class="abs voucher__badge"><span>10%</span><span>OFF</span></div>
  <p class="abs voucher__items center">Plants<br>Giftware<br>&amp;<br>Pet Supplies</p>
  <p class="abs voucher__small center">dog food and vet meds not included</p>

  <div class="abs hours center">
    <p class="hours__title">Opening Hours</p>
    <p>Mon-Friday 8.30 - 5.00</p>
    <p>Saturday 8.30-3.00</p>
    <p>Sunday 9.30 - 1.30</p>
  </div>

  <div class="abs brand brand--panel"><span class="brand__dot"></span>THE COPPER MEADOW</div>

  <div class="abs contact center">
    <p class="contact__phone">Call Now 07 4000 2718</p>
    <p>1280, Meridian Highway,<br>Tallowbrook Q 4790</p>
  </div>

  <div class="abs brand brand--cover"><span class="brand__dot"></span>THE COPPER MEADOW</div>
  <p class="abs cover__tagline center">Pets, Plants<br>Giftware &amp; Produce</p>
</section>

<section class="sheet sheet--inside" aria-label="Brochure inside">
  <svg class="sheet__art" viewBox="0 0 778 549">
    <defs>
      <linearGradient id="g-pup" x1="0" y1="0" x2="1" y2="1"><stop offset="0" stop-color="#f4f4f4"/><stop offset="1" stop-color="#9a9a9a"/></linearGradient>
      <radialGradient id="g-fish"><stop offset="0" stop-color="#f59a7a"/><stop offset="1" stop-color="#3b3b3b"/></radialGradient>
      <linearGradient id="g-garden" x1="0" y1="0" x2="1" y2="1"><stop offset="0" stop-color="#3f6a35"/><stop offset=".5" stop-color="#a8b39b"/><stop offset="1" stop-color="#4c7a3d"/></linearGradient>
      <linearGradient id="g-hens" x1="0" y1="0" x2="1" y2="0"><stop offset="0" stop-color="#d9d1c7"/><stop offset=".6" stop-color="#6b4a33"/><stop offset="1" stop-color="#b8652c"/></linearGradient>
      <linearGradient id="g-bags" x1="0" y1="0" x2="1" y2="0"><stop offset="0" stop-color="#e8e8e8"/><stop offset=".5" stop-color="#5a5a5a"/><stop offset="1" stop-color="#d4d4d4"/></linearGradient>
      <linearGradient id="g-pots" x1="0" y1="0" x2="0" y2="1"><stop offset="0" stop-color="#ffffff"/><stop offset=".4" stop-color="#e9a06b"/><stop offset="1" stop-color="#d88447"/></linearGradient>
      <linearGradient id="g-feeders" x1="0" y1="0" x2="1" y2="0"><stop offset="0" stop-color="#f7f7f7"/><stop offset=".6" stop-color="#d9e9c4"/><stop offset="1" stop-color="#c9b27a"/></linearGradient>
    </defs>
    <rect x="0" y="0" width="259" height="549" fill="var(--green)"/>
    <path d="M0 0 H165 C205 60 200 150 150 192 C110 218 40 205 0 188 Z" fill="url(#g-pup)" role="img" aria-label="Photo of a dalmatian puppy"/>
    <path d="M165 0 C205 60 200 150 150 192 C110 218 40 205 0 188" fill="none" stroke="var(--blue)" stroke-width="5"/>
    <path d="M160 0 H259 V110 C230 90 200 95 185 100 C195 60 185 25 160 0 Z" fill="#fff"/>
    <path d="M175 0 H185 C205 30 210 70 200 100 L190 100 C200 70 195 30 175 0 Z" fill="var(--blue)"/>
    <circle cx="190" cy="150" r="50" fill="url(#g-fish)" stroke="var(--green-dark)" stroke-width="5" role="img" aria-label="Photo of an orange tropical aquarium fish"/>
    <rect x="0" y="376" width="259" height="173" fill="url(#g-bags)" role="img" aria-label="Photo of stacked bags of dry dog and cat food"/>
    <rect x="259" y="0" width="260" height="549" fill="#fff"/>
    <rect x="259" y="0" width="260" height="170" fill="url(#g-garden)" role="img" aria-label="Photo of a stepping-stone garden path lined with ferns"/>
    <path d="M259 150 C340 165 430 150 519 130 V400 C430 385 340 392 259 405 Z" fill="var(--blue)"/>
    <path d="M259 130 C340 150 430 140 519 115 V130 C430 152 340 165 259 150 Z" fill="var(--green)"/>
    <path d="M259 405 C340 392 430 385 519 400 V404 C430 390 340 397 259 410 Z" fill="var(--pink)"/>
    <path d="M259 420 C360 408 440 412 519 428 V440 C440 425 360 422 259 432 Z" fill="var(--brown)"/>
    <rect x="259" y="445" width="260" height="104" fill="url(#g-pots)" role="img" aria-label="Photo of three terracotta pots"/>
    <rect x="519" y="0" width="259" height="549" fill="var(--pink)"/>
    <path d="M519 0 H778 V78 C700 100 610 125 519 120 Z" fill="url(#g-hens)" role="img" aria-label="Photo of laying hens in a yard"/>
    <path d="M519 120 C610 125 700 100 778 78 V92 C700 115 610 138 519 134 Z" fill="var(--blue)"/>
    <path d="M519 134 C610 138 700 115 778 92 V100 C700 125 610 148 519 142 Z" fill="var(--green)"/>
    <rect x="519" y="437" width="259" height="112" fill="url(#g-feeders)" role="img" aria-label="Photo of poultry feeders, drinkers and feed sacks"/>
  </svg>

  <div class="tag tag--pets">Pets</div>
  <ul class="list list--pet-a"><li>Puppies &amp; Kittens</li><li>Guinea pigs &amp; Mice</li></ul>
  <ul class="list list--pet-b"><li>Birds &amp; Hermit Crabs</li><li>Huge range of Fish &amp; Aquatic Plants</li></ul>
  <div class="tag tag--stock">Stock Includes</div>
  <ul class="list list--stock-a"><li>Fish Tanks</li><li>Aquarium Accessories and Food</li><li>Bird Cages &amp; Nesting Boxes</li></ul>
  <ul class="list list--stock-b"><li>Small animal pens and cages</li><li>Dog Food: Northvale, Iron Kite, Canix, Dogmax and Bramble</li></ul>

  <ul class="list list--white list--plants">
    <li>Plants (&amp; Giftware)</li>
    <li>Palms &amp; Staghorns</li>
    <li>Natives &amp; Cycads</li>
    <li>Huge range of Indoor Plants &amp; Ferns<br>Pines and Trees</li>
    <li>Groundcovers and Hedging</li>
    <li class="tight">Giftware</li>
    <li class="tight">Statues and Water Features</li>
    <li>Indoor and Outdoor pots</li>
  </ul>
  <p class="abs fine">Landscaper Discounts Apply</p>

  <div class="tag tag--produce">Produce</div>
  <ul class="list list--white list--produce"><li>Hay &amp; Chaff</li><li>Hartfield &amp; Soyamax</li><li>Chook Food</li><li>Chickens and Layer Hens</li><li>Horse and Cattle Feed</li></ul>
  <div class="tag tag--grain">Mixed Grain</div>
  <ul class="list list--white list--grain"><li>Bulk Dog Food</li><li>Chicken Feeders &amp; Drinkers</li><li>Special Orders Welcome</li></ul>
</section>

</body>
</html>
```